Design New Business Card, Envelope and Letter Head !

We need a stationery design for our newly developed logo! We need professional classic look.

Front of the Card:
Logo on the left hand side

Personal Detail in the right hand side
i.e. Name,
Title
Office:
Cell:
Fax:
email:

www.corvelmortgage.example

Color Scheme should match our logo.

Back Side of the Card:

Logo again with Green back ground or off gray back ground ( Note: Color has to be from logo)

and below message. Again, font size and color should come from logo.

" Manifest your trust in us through the gift of your referrals. We won't let you down."
Updates

Dear Designers;

We have updates few info which we missed earlier. Please include those words in the logo and resubmit your designs for consideration.  We are looking for very professional and classic look. Thanks for your great creation. I have changed the payment options. Please have a look and best of luck.

Tobin

Dear All Designers:

For address; please use following address:

" 4719 Copper Glen Ln, San Ramon, CA 94583 " 
Please do not use the address in the website. We would like to give business card with option of calling us is the top priority then email then eFax. Please make sure Put " eFax" in the business card. 

Reason: Since I have updated some information per requirements, I would like to give enough time for the great design work.

Just a note to all designers:

"Equal Opportunity Lender" Sign has to be in back  of the card  in a small image. I would say it has to be "inconspicuous". Let's put the NMLS # and CalBRE # in front side. Let's organise the information follow very elegant and professional.

Requirements
Must have
• We must need following Words in the business card

CalBRE License #

NMLS #

And the logo of " Equal Housing Lender ". Please see the logo attached.

Please put these words or logo represents above at the right location of the card.

```html
<!DOCTYPE html>
<html lang="en">
<head>
<meta charset="utf-8">
<title>Corvelline Lending Stationery</title>
<link rel="stylesheet" href="https://fonts.googleapis.com/css2?family=Libre+Baskerville&family=Open+Sans:wght@400;600&display=swap">
<style>
:root{
  --green:#6aad50;
  --green-dark:#5a9a43;
  --grey:#666a6c;
  --grey-dark:#4e5254;
  --paper:#ffffff;
  --stage:#ececec;
  --ink:#444;
  --muted:#666;
}
*{box-sizing:border-box;margin:0;padding:0}
html,body{width:1200px;height:1000px;overflow:hidden;background:var(--stage)}
body{position:relative;font-family:"Open Sans",Arial,sans-serif;color:var(--ink)}
.sheet{position:absolute;background:var(--paper);box-shadow:0 2px 8px rgba(0,0,0,.12);overflow:hidden}
.brand{font-family:"Libre Baskerville",Georgia,serif;color:var(--grey-dark);display:flex;align-items:center;gap:8px;white-space:nowrap}
.brand-mark{background:var(--green);flex:none}
.icon{width:9px;height:9px;flex:none;color:var(--green)}
.contact-row{display:flex;align-items:center;gap:5px;color:var(--muted)}

/* business card back */
.card-back{left:60px;top:60px;width:300px;height:172px;background:var(--green);display:flex;flex-direction:column;align-items:center;justify-content:center;gap:10px;padding:0 24px}
.card-back .brand{color:#fff;font-size:19px}
.card-back .brand-mark{background:#fff;width:14px;height:14px}
.card-back .message{color:#fff;font-size:9px;text-align:center;line-height:1.5}
.card-back .lender-badge{position:absolute;right:12px;bottom:10px;width:16px;height:16px;border:1.5px solid #fff}

/* business card front */
.card-front{left:390px;top:60px;width:300px;height:172px;display:flex}
.card-front .logo-side{width:106px;padding:14px 10px}
.card-front .logo-side .brand{font-size:11px;gap:6px;white-space:normal;align-items:flex-start;line-height:1.3}
.card-front .brand-mark{width:8px;height:8px;margin-top:3px}
.card-front .strip{width:8px;background:var(--grey)}
.card-front .strip-green{width:4px;background:var(--green-dark)}
.card-front .detail-side{flex:1;background:var(--green);color:#fff;padding:16px 14px;font-size:7.5px;display:flex;flex-direction:column;gap:4px}
.card-front .detail-side .contact-row,.card-front .detail-side .icon{color:#fff}
.card-front .person-name{font-family:"Libre Baskerville",Georgia,serif;font-size:15px;color:#fff}
.card-front .person-title{font-size:8px;margin-bottom:6px;opacity:.9}
.card-front .licences{margin-top:auto;font-size:6.5px;opacity:.9;white-space:nowrap}

/* envelope front */
.envelope-front{left:60px;top:270px;width:580px;height:290px}
.envelope-front .bar-grey{position:absolute;left:0;top:0;width:10px;height:110px;background:var(--grey)}
.envelope-front .bar-green{position:absolute;left:0;top:110px;width:10px;height:180px;background:var(--green)}
.envelope-front .logo-block{position:absolute;left:30px;top:120px}
.envelope-front .brand{font-size:17px}
.envelope-front .brand-mark{width:12px;height:12px}

/* envelope back */
.envelope-back{left:60px;top:590px;width:580px;height:290px}
.envelope-back .flap{position:absolute;left:0;top:0;width:100%;height:96px;background:var(--green);border-bottom-right-radius:38px}
.envelope-back .return-block{position:absolute;right:40px;top:118px;width:190px;font-size:7.5px;display:flex;flex-direction:column;gap:3px}
.envelope-back .brand{font-size:13px;margin-bottom:5px}
.envelope-back .brand-mark{width:10px;height:10px}

/* letterhead */
.letterhead{left:690px;top:60px;width:450px;height:636px}
.letterhead .logo-block{position:absolute;right:50px;top:52px}
.letterhead .brand{font-size:24px}
.letterhead .brand-mark{width:16px;height:16px}
.letterhead .letter-body{position:absolute;left:50px;right:50px;top:140px;font-size:8px;line-height:1.55;color:#555}
.letterhead .letter-body p{margin-bottom:12px}
.letterhead .signature{display:block;width:110px;height:34px;margin:16px 0 0 140px;background:linear-gradient(90deg,#e8e8e8,#d2d2d2)}
.letterhead .footer-contacts{position:absolute;left:30px;bottom:30px;display:flex;flex-wrap:wrap;gap:4px 12px;width:260px;font-size:6.5px}
.letterhead .footer-grey{position:absolute;left:0;bottom:0;width:290px;height:9px;background:var(--grey)}
.letterhead .footer-green{position:absolute;right:0;bottom:0;width:160px;height:42px;background:var(--green);display:flex;align-items:center;justify-content:center}
.letterhead .footer-green .brand{color:#fff;font-size:11px}
</style>
</head>
<body>

<svg width="0" height="0" style="position:absolute">
  <defs>
    <symbol id="i-phone" viewBox="0 0 10 10"><path d="M2 1l2 2-1 1.2a6 6 0 0 0 2.8 2.8L7 6l2 2-1.4 1.4C4.5 9.4.6 5.5.6 2.4z" fill="currentColor"/></symbol>
    <symbol id="i-pin" viewBox="0 0 10 10"><path d="M5 .5a3.3 3.3 0 0 1 3.3 3.3C8.3 6.3 5 9.5 5 9.5S1.7 6.3 1.7 3.8A3.3 3.3 0 0 1 5 .5z" fill="currentColor"/><circle cx="5" cy="3.8" r="1.2" fill="#fff"/></symbol>
    <symbol id="i-mail" viewBox="0 0 10 10"><rect x=".5" y="2" width="9" height="6.5" fill="currentColor"/><path d="M.8 2.3L5 5.8l4.2-3.5" stroke="#fff" stroke-width=".8" fill="none"/></symbol>
    <symbol id="i-globe" viewBox="0 0 10 10"><circle cx="5" cy="5" r="4.3" fill="none" stroke="currentColor" stroke-width="1"/><path d="M.8 5h8.4M5 .7c-2.4 2.6-2.4 6 0 8.6M5 .7c2.4 2.6 2.4 6 0 8.6" stroke="currentColor" stroke-width=".8" fill="none"/></symbol>
  </defs>
</svg>

<section class="sheet card-back">
  <div class="brand"><span class="brand-mark"></span>Corvelline Lending</div>
  <p class="message">Manifest your trust in us through the gift of your referrals. We won't let you down.</p>
  <span class="lender-badge" role="img" aria-label="Equal housing lender badge"></span>
</section>

<section class="sheet card-front">
  <div class="logo-side">
    <div class="brand"><span class="brand-mark"></span><span>Corvelline Lending</span></div>
  </div>
  <div class="strip"></div>
  <div class="strip-green"></div>
  <div class="detail-side">
    <div class="person-name">Dana Whitlow</div>
    <div class="person-title">Senior Mortgage Advisor</div>
    <div class="contact-row"><svg class="icon"><use href="#i-phone"/></svg>Office: 555-0148-27</div>
    <div class="contact-row"><svg class="icon"><use href="#i-phone"/></svg>Cell: 555-0148-31</div>
    <div class="contact-row"><svg class="icon"><use href="#i-mail"/></svg>eFax: 555-0148-40</div>
    <div class="contact-row"><svg class="icon"><use href="#i-globe"/></svg>www.corvelmortgage.example</div>
    <div class="licences">NMLS # 000000 &nbsp;|&nbsp; CalBRE License # 00000000</div>
  </div>
</section>

<section class="sheet envelope-front">
  <div class="bar-grey"></div>
  <div class="bar-green"></div>
  <div class="logo-block">
    <div class="brand"><span class="brand-mark"></span>Corvelline Lending</div>
  </div>
</section>

<section class="sheet envelope-back">
  <div class="flap"></div>
  <div class="return-block">
    <div class="brand"><span class="brand-mark"></span>Corvelline Lending</div>
    <div class="contact-row"><svg class="icon"><use href="#i-pin"/></svg>4719 Copper Glen Ln, San Ramon, CA 94583</div>
    <div class="contact-row"><svg class="icon"><use href="#i-phone"/></svg>555-0148-27</div>
    <div class="contact-row"><svg class="icon"><use href="#i-mail"/></svg>hello@corvelmortgage.example</div>
    <div class="contact-row"><svg class="icon"><use href="#i-globe"/></svg>www.corvelmortgage.example</div>
  </div>
</section>

<section class="sheet letterhead">
  <div class="logo-block">
    <div class="brand"><span class="brand-mark"></span>Corvelline Lending</div>
  </div>
  <div class="letter-body">
    <p>Dear Client,</p>
    <p>Lorem ipsum dolor sit amet, consectetur adipiscing elit. Nulla sodales nisi vitae lorem ipsum dolor sit amet, consectetur adipiscing elit. Suspendisse feugiat eros nisl, a facilisis risus eleifend sed. Aliquam mauris enim, fermentum eu lacinia sit amet, laoreet eu leo. Nullam eleifend nulla at libero tristique, ac vulputate odio tincidunt. Etiam non condimentum tortor. Integer suscipit neque nec odio porttitor cursus. Phasellus a sapien blandit, suscipit justo id, condimentum ante. Morbi tristique justo risus, id mattis dui molestie ut. Nullam volutpat ut quam commodo faucibus. Pellentesque urna est, interdum in elit quis, pharetra elementum orci. Nam pharetra velit molestie justo placerat scelerisque.</p>
    <p>Ut vitae interdum diam, in euismod ante. Pellentesque volutpat, risus sit amet sodales hendrerit, mi turpis vulputate dolor, eget cursus nulla eros nec tellus. Nulla tincidunt molestie libero vel pretium. Donec condimentum nulla sit amet risus semper imperdiet. Duis congue eros nec diam blandit, et pellentesque sapien auctor. Curabitur iaculis enim lectus, in imperdiet mauris mattis eget. Etiam ac ornare metus. Mauris risus leo, egestas at dolor a, ultrices adipiscing est. Nunc faucibus scelerisque mollis. Pellentesque aliquet mauris tellus, id dignissim risus viverra et. Mauris venenatis lobortis eros. Nam id diam in ligula malesuada feugiat. Cras turpis felis, aliquet id mauris elementum, feugiat ultricies nisl.</p>
    <p>Best regards,</p>
    <span class="signature" role="img" aria-label="Handwritten signature of Dana Whitlow"></span>
  </div>
  <div class="footer-contacts">
    <span class="contact-row"><svg class="icon"><use href="#i-phone"/></svg>555-0148-27</span>
    <span class="contact-row"><svg class="icon"><use href="#i-pin"/></svg>4719 Copper Glen Ln, San Ramon, CA 94583</span>
    <span class="contact-row"><svg class="icon"><use href="#i-mail"/></svg>hello@corvelmortgage.example</span>
    <span class="contact-row"><svg class="icon"><use href="#i-globe"/></svg>www.corvelmortgage.example</span>
  </div>
  <div class="footer-grey"></div>
  <div class="footer-green"><div class="brand">Corvelline Lending</div></div>
</section>

</body>
</html>
```